Elegant, professional powerpoint design for Varomel Engineering and Mining SARLU

I’ve created a new Sub contracting company for mining industry in the Democratic Republic of Congo. With Quorvixel, I’ve created a logo. I would want a professional and beautiful powerpoint design which I will use to sell my services to mining companies in DRC. The powerpoint must have pictures of mining engines such as excavators, drones, trucks, etc

```html
<!DOCTYPE html>
<html lang="en">
<head>
<meta charset="utf-8">
<title>Varomel Engineering and Mining – Presentation</title>
<link rel="stylesheet" href="https://fonts.googleapis.com/css2?family=Poppins:wght@400;500;600;700;800&display=swap">
<style>
:root{
  --page:#cde8fb;
  --navy:#1b2a92;
  --navy-deep:#141f6e;
  --gold:#e08f0c;
  --gold-dark:#8a5510;
  --white:#ffffff;
  --grey:#6d6d6d;
  --frame-light:rgba(255,255,255,.85);
}
*{margin:0;padding:0;box-sizing:border-box}
html,body{width:1200px;height:4104px;overflow:hidden;background:var(--page);font-family:"Poppins",sans-serif}
.slide{position:absolute;left:35px;width:1130px;height:635px;overflow:hidden;color:var(--white)}
.slide.dark{background:linear-gradient(180deg,#1c2b98 0%,#2f3a8c 40%,#5b4c55 70%,#7c5a22 100%)}
.slide.light{background:var(--white)}
.scene{position:absolute;inset:0}
.scene.hills{background:
  radial-gradient(ellipse 40% 55% at 12% 62%,rgba(40,60,30,.55),transparent 70%),
  radial-gradient(ellipse 70% 35% at 60% 95%,rgba(170,140,40,.45),transparent 75%),
  linear-gradient(180deg,rgba(40,50,150,0) 40%,rgba(150,120,40,.35) 100%)}
.scene.pit{background:
  radial-gradient(ellipse 55% 18% at 78% 10%,rgba(120,125,170,.35),transparent 75%),
  linear-gradient(180deg,rgba(40,50,150,0) 40%,rgba(150,120,40,.35) 100%)}
.scene.truck{background:
  radial-gradient(ellipse 30% 35% at 50% 30%,rgba(70,70,90,.35),transparent 75%),
  linear-gradient(180deg,rgba(40,50,150,0) 40%,rgba(150,120,40,.35) 100%)}
.frame{position:absolute;inset:22px;border:2px solid var(--frame-light);pointer-events:none}
.light .frame{border-color:var(--navy);border-bottom-color:var(--gold-dark);border-right-color:#a08a6a}
.brand-sm{position:absolute;left:42px;top:60px;width:130px;font-weight:700;color:var(--white);text-align:center;line-height:1}
.brand-sm .n{font-size:22px;letter-spacing:1px}
.brand-sm .s{font-size:6.5px;letter-spacing:.4px;margin-top:3px}
.light .brand-sm{color:var(--navy)}
.h2{position:absolute;font-weight:800;font-size:46px;line-height:1;letter-spacing:1px}
.photo{position:absolute}
/* cover */
.hero-dot{position:absolute;left:505px;top:150px;width:120px;height:120px;border-radius:50%;background:var(--white)}
.hero-name{position:absolute;left:0;right:0;top:404px;text-align:center;font-weight:700;line-height:1}
.hero-name .n{font-size:82px;letter-spacing:3px}
.hero-name .s{font-size:31px;letter-spacing:3px;margin-top:18px}
.body-copy{position:absolute;font-size:15.5px;line-height:24px;font-weight:400}
/* services */
.services-title{color:var(--navy);left:0;right:0;text-align:center;top:62px;font-size:44px}
.core{position:absolute;left:419px;top:226px;width:290px;height:290px;border-radius:50%;background:linear-gradient(180deg,#f0a21a,#8a5510);display:flex;align-items:center;justify-content:center;font-weight:700;font-size:40px;color:var(--white);letter-spacing:2px}
.links{position:absolute;inset:0}
.svc{position:absolute;width:260px;color:var(--navy)}
.svc h3{font-size:23px;font-weight:700;line-height:1.1;white-space:nowrap}
.svc p{font-size:11.5px;color:var(--grey);line-height:16px;margin-top:10px;width:225px}
.icon{position:absolute;width:70px;height:70px;border-radius:50%;background:var(--navy-deep);border:3px solid var(--gold);display:flex;align-items:center;justify-content:center}
/* team */
.member{position:absolute;width:243px;text-align:center}
.member svg{display:block;margin:0 auto}
.member h4{font-size:22px;font-weight:500;letter-spacing:.5px;white-space:nowrap}
.member p{font-size:12.3px;line-height:19px;margin-top:10px}
/* end */
.end-dot{position:absolute;left:520px;top:100px;width:90px;height:90px;border-radius:50%;background:var(--white)}
.end-name{position:absolute;left:0;right:0;top:226px;text-align:center;font-weight:700;line-height:1}
.end-name .n{font-size:46px;letter-spacing:2px}
.end-name .s{font-size:19px;letter-spacing:2px;margin-top:8px}
.thanks{position:absolute;left:0;width:1076px;top:338px;text-align:center;font-size:82px;font-weight:800;letter-spacing:2px;line-height:1}
.contact{position:absolute;top:481px;display:flex;align-items:center;gap:16px;font-size:12.5px;line-height:19px}
.contact .ic{width:38px;height:38px;border-radius:50%;background:var(--white);display:flex;align-items:center;justify-content:center;flex:none}
</style>
</head>
<body>

<section class="slide dark" style="top:32px">
  <div class="scene hills" role="img" aria-label="Misty hillside landscape at a mining region"></div>
  <div class="frame"></div>
  <div class="hero-dot"></div>
  <div class="hero-name"><div class="n">VAROMEL</div><div class="s">ENGINEERING AND MINING</div></div>
</section>

<section class="slide dark" style="top:701px">
  <div class="scene pit" role="img" aria-label="Open pit mine terraces in the background"></div>
  <div class="frame"></div>
  <div class="brand-sm"><div class="n">VAROMEL</div><div class="s">ENGINEERING AND MINING</div></div>
  <div class="photo" style="left:231px;top:40px;width:282px;height:263px;background:radial-gradient(ellipse 45% 35% at 50% 52%,#e2a51c,rgba(226,165,28,0) 80%),radial-gradient(ellipse 40% 18% at 48% 22%,#2e2a26,rgba(46,42,38,0) 80%),linear-gradient(180deg,#9a9a9a,#7e7e7e 55%,#4c4c4c)" role="img" aria-label="Yellow mining haul truck loaded with ore"></div>
  <div class="photo" style="left:521px;top:113px;width:282px;height:270px;background:radial-gradient(ellipse 30% 30% at 62% 55%,#f3d7b0,rgba(243,215,176,0) 75%),radial-gradient(ellipse 45% 40% at 30% 35%,#c76a33,rgba(199,106,51,0) 75%),linear-gradient(160deg,#2b2320,#8a4a2a 55%,#1e1a18)" role="img" aria-label="Miner drilling rock underground"></div>
  <div class="photo" style="left:811px;top:196px;width:283px;height:391px;background:radial-gradient(circle at 62% 28%,#8c6f70 0,#5a4a4c 22%,rgba(60,52,52,0) 45%),linear-gradient(180deg,#8a8686,#4a4444 50%,#202020)" role="img" aria-label="Bucket wheel excavator over coal pile"></div>
  <div class="h2" style="left:53px;top:344px">MINING INDUSTRY</div>
  <p class="body-copy" style="left:53px;top:414px;width:735px">Sed ut perspiciatis unde omnis iste natus error sit voluptatem accusantium doloremque laudantium, totam rem aperiam, eaque ipsa quae ab illo inventore veritatis et quasi architecto beatae vitae dicta sunt explicabo. Nemo enim ipsam voluptatem quia voluptas sit aspernatur aut odit aut fugit, sed quia consequuntur magni dolores eos qui ratione voluptatem sequi nesciunt. Neque porro quisquam est, qui dolorem ipsum quia dolor sit amet, consectetur, adipisci velit, sed quia non numquam eius modi tempora incidunt ut labore et dolore magnam aliquam quaerat voluptatem.</p>
</section>

<section class="slide dark" style="top:1368px">
  <div class="scene pit" role="img" aria-label="Open pit mine terraces in the background"></div>
  <div class="frame"></div>
  <div class="brand-sm"><div class="n">VAROMEL</div><div class="s">ENGINEERING AND MINING</div></div>
  <div class="h2" style="left:362px;top:59px">MINING ENGINES</div>
  <div class="photo" style="left:51px;top:142px;width:496px;height:454px;border:1px dashed rgba(255,255,255,.6);background:radial-gradient(ellipse 14% 10% at 77% 63%,#e3a21c,rgba(227,162,28,0) 85%),radial-gradient(ellipse 60% 30% at 50% 35%,#e8e8e8,rgba(232,232,232,0) 80%),linear-gradient(180deg,#6a6a6a,#cfcfcf 40%,#5a5a5a 75%,#1c1c1c)" role="img" aria-label="Crawler excavator with raised arm on a rock field"></div>
  <p class="body-copy" style="left:579px;top:143px;width:490px;font-size:16px;line-height:25.8px">Sed ut perspiciatis unde omnis iste natus error sit voluptatem accusantium doloremque laudantium, totam rem aperiam, eaque ipsa quae ab illo inventore veritatis et quasi architecto beatae vitae dicta sunt explicabo. Nemo enim ipsam voluptatem quia voluptas sit aspernatur aut odit aut fugit, sed quia consequuntur magni dolores eos qui ratione voluptatem sequi nesciunt. Neque porro quisquam est, qui dolorem ipsum quia dolor sit amet, consectetur, adipisci velit, sed quia non numquam eius modi tempora incidunt ut labore et dolore magnam aliquam quaerat voluptatem. Sed ut perspiciatis unde omnis iste natus error sit voluptatem accusantium doloremque laudantium Sed ut perspiciatis unde omnis iste natus error sit voluptatem accusantium doloremque laudantium, totam rem aperiam, eaque ipsa quae ab illo inventore veritatis et quasi architecto beatae vitae dicta sunt explicabo. Nemo enim ipsam voluptatem quia voluptas sit aspernatur aut odit aut</p>
</section>

<section class="slide light" style="top:2045px">
  <div class="frame"></div>
  <div class="brand-sm"><div class="n">VAROMEL</div><div class="s">ENGINEERING AND MINING</div></div>
  <div class="h2 services-title">OUR SERVICES</div>
  <div class="core">VAROMEL</div>
  <svg class="links" width="1130" height="635" viewBox="0 0 1130 635" fill="none" stroke="#555" stroke-width="1.3" stroke-dasharray="4 3">
    <polyline points="178,203 425,203 469,263"/>
    <polyline points="172,365 425,365"/>
    <polyline points="178,532 420,532 469,481"/>
    <polyline points="952,203 705,203 661,263"/>
    <polyline points="958,365 705,365"/>
    <polyline points="952,532 710,532 661,481"/>
    <g fill="#8a5510" stroke="none">
      <circle cx="469" cy="263" r="8"/><circle cx="425" cy="365" r="8"/><circle cx="469" cy="481" r="8"/>
      <circle cx="661" cy="263" r="8"/><circle cx="705" cy="365" r="8"/><circle cx="661" cy="481" r="8"/>
    </g>
  </svg>

  <div class="icon" style="left:97px;top:169px"><svg width="34" height="34" viewBox="0 0 24 24" fill="none" stroke="#fff" stroke-width="1.4"><circle cx="10" cy="7" r="4"/><path d="M3 21c0-4 3-7 7-7s7 3 7 7"/><circle cx="18" cy="17" r="2.5"/></svg></div>
  <div class="svc" style="left:178px;top:178px"><h3>Lorem ipsum dolor</h3><p>Sed ut perspiciatis unde omnis iste natus error sit voluptatem accusantium doloremque</p></div>

  <div class="icon" style="left:91px;top:330px"><svg width="34" height="34" viewBox="0 0 24 24" fill="none" stroke="#fff" stroke-width="1.4"><circle cx="12" cy="12" r="3.5"/><path d="M12 2v3M12 19v3M2 12h3M19 12h3M4.9 4.9l2.1 2.1M17 17l2.1 2.1M4.9 19.1L7 17M17 7l2.1-2.1"/></svg></div>
  <div class="svc" style="left:172px;top:340px"><h3>Lorem ipsum dolor</h3><p>Sed ut perspiciatis unde omnis iste natus error sit voluptatem accusantium doloremque</p></div>

  <div class="icon" style="left:97px;top:497px"><svg width="34" height="34" viewBox="0 0 24 24" fill="none" stroke="#fff" stroke-width="1.4"><path d="M6 16a4 4 0 010-8 6 6 0 0111.5 1.5A3.5 3.5 0 0118 16z"/><path d="M9 12l2 2 4-4"/></svg></div>
  <div class="svc" style="left:178px;top:507px"><h3>Lorem ipsum dolor</h3><p>Sed ut perspiciatis unde omnis iste natus error sit voluptatem accusantium doloremque</p></div>

  <div class="icon" style="left:961px;top:169px"><svg width="34" height="34" viewBox="0 0 24 24" fill="none" stroke="#fff" stroke-width="1.4"><circle cx="12" cy="7" r="4"/><rect x="5" y="13" width="14" height="8" rx="1"/><path d="M10 16l-1.5 1.5L10 19M14 16l1.5 1.5L14 19"/></svg></div>
  <div class="svc" style="left:715px;top:178px"><h3>Lorem ipsum dolor</h3><p>Sed ut perspiciatis unde omnis iste natus error sit voluptatem accusantium doloremque</p></div>

  <div class="icon" style="left:967px;top:330px"><svg width="34" height="34" viewBox="0 0 24 24" fill="none" stroke="#fff" stroke-width="1.4"><circle cx="12" cy="14" r="5"/><path d="M10 14l1.5 1.5L14.5 12.5M12 9V3M7 10L4 6M17 10l3-4"/></svg></div>
  <div class="svc" style="left:720px;top:340px"><h3>Lorem ipsum dolor</h3><p>Sed ut perspiciatis unde omnis iste natus error sit voluptatem accusantium doloremque</p></div>

  <div class="icon" style="left:961px;top:497px"><svg width="34" height="34" viewBox="0 0 24 24" fill="none" stroke="#fff" stroke-width="1.4"><rect x="3" y="4" width="18" height="12" rx="1"/><path d="M9 20h6M12 16v4M9 10l2 2 4-4"/></svg></div>
  <div class="svc" style="left:715px;top:507px"><h3>Lorem ipsum dolor</h3><p>Sed ut perspiciatis unde omnis iste natus error sit voluptatem accusantium doloremque</p></div>
</section>

<section class="slide dark" style="top:2729px">
  <div class="scene truck" role="img" aria-label="Haul truck silhouette in the background"></div>
  <div class="frame"></div>
  <div class="brand-sm"><div class="n">VAROMEL</div><div class="s">ENGINEERING AND MINING</div></div>
  <div class="h2" style="left:0;right:0;text-align:center;top:74px">OUR TEAM</div>

  <div class="member" style="left:51px;top:191px">
    <svg width="243" height="252" viewBox="0 0 243 252"><defs><linearGradient id="p1" x1="0" y1="0" x2="0" y2="1"><stop offset="0" stop-color="#a7adb8"/><stop offset="1" stop-color="#7d8390"/></linearGradient></defs><polygon points="121.5,4 239,66 239,186 121.5,248 4,186 4,66" fill="#b06f0e"/><polygon points="121.5,22 222,75 222,177 121.5,230 21,177 21,75" fill="url(#p1)" role="img" aria-label="Portrait of team member holding a clipboard"/></svg>
    <h4 style="margin-top:44px">MARA KELNOR</h4>
    <p>Lorem ipsum dolor sit amet, consectetur adipiscing elit, sed do eiusmod tempor incididunt ut labore et dolore magna</p>
  </div>
  <div class="member" style="left:315px;top:164px">
    <svg width="243" height="252" viewBox="0 0 243 252"><defs><linearGradient id="p2" x1="0" y1="0" x2="0" y2="1"><stop offset="0" stop-color="#c4c7ce"/><stop offset="1" stop-color="#5b6f96"/></linearGradient></defs><polygon points="121.5,4 239,66 239,186 121.5,248 4,186 4,66" fill="#b06f0e"/><polygon points="121.5,22 222,75 222,177 121.5,230 21,177 21,75" fill="url(#p2)" role="img" aria-label="Portrait of team member in a grey blazer"/></svg>
    <h4 style="margin-top:40px">LINA DOVAR</h4>
    <p>Lorem ipsum dolor sit amet, consectetur adipiscing elit, sed do eiusmod tempor incididunt ut labore et dolore magna</p>
  </div>
  <div class="member" style="left:580px;top:191px">
    <svg width="243" height="252" viewBox="0 0 243 252"><defs><linearGradient id="p3" x1="0" y1="0" x2="0" y2="1"><stop offset="0" stop-color="#d6d6d6"/><stop offset="1" stop-color="#6e6f73"/></linearGradient></defs><polygon points="121.5,4 239,66 239,186 121.5,248 4,186 4,66" fill="#b06f0e"/><polygon points="121.5,22 222,75 222,177 121.5,230 21,177 21,75" fill="url(#p3)" role="img" aria-label="Portrait of team member in a grey suit"/></svg>
    <h4 style="margin-top:44px">INES TALVO</h4>
    <p>Lorem ipsum dolor sit amet, consectetur adipiscing elit, sed do eiusmod tempor incididunt ut labore et dolore magna</p>
  </div>
  <div class="member" style="left:846px;top:164px">
    <svg width="243" height="252" viewBox="0 0 243 252"><defs><linearGradient id="p4" x1="0" y1="0" x2="0" y2="1"><stop offset="0" stop-color="#cdd4d8"/><stop offset="1" stop-color="#262a3a"/></linearGradient></defs><polygon points="121.5,4 239,66 239,186 121.5,248 4,186 4,66" fill="#b06f0e"/><polygon points="121.5,22 222,75 222,177 121.5,230 21,177 21,75" fill="url(#p4)" role="img" aria-label="Portrait of team member in a dark suit"/></svg>
    <h4 style="margin-top:46px">JON PRESK</h4>
    <p>Lorem ipsum dolor sit amet, consectetur adipiscing elit, sed do eiusmod tempor incididunt ut labore et dolore magna</p>
  </div>
</section>

<section class="slide dark" style="top:3408px">
  <div class="scene hills" role="img" aria-label="Misty hillside landscape at a mining region"></div>
  <div class="frame"></div>
  <div class="end-dot"></div>
  <div class="end-name"><div class="n">VAROMEL</div><div class="s">ENGINEERING AND MINING</div></div>
  <div class="thanks">THANK YOU</div>
  <div class="contact" style="left:117px">
    <span class="ic"><svg width="18" height="18" viewBox="0 0 24 24" fill="#1b2a92"><path d="M12 2a7 7 0 00-7 7c0 5 7 13 7 13s7-8 7-13a7 7 0 00-7-7zm0 9.5A2.5 2.5 0 1112 6.5a2.5 2.5 0 010 5z"/></svg></span>
    <span>1417 Lorem ipsum dolor sit amet,<br>consectetur adipiscing elit</span>
  </div>
  <div class="contact" style="left:492px">
    <span class="ic"><svg width="18" height="18" viewBox="0 0 24 24" fill="#1b2a92"><path d="M6.6 10.8a15.1 15.1 0 006.6 6.6l2.2-2.2a1 1 0 011-.25 11.4 11.4 0 003.6.57 1 1 0 011 1V20a1 1 0 01-1 1A17 17 0 013 4a1 1 0 011-1h3.5a1 1 0 011 1 11.4 11.4 0 00.57 3.6 1 1 0 01-.25 1z"/></svg></span>
    <span>+1 888 8888 8888</span>
  </div>
  <div class="contact" style="left:736px">
    <span class="ic"><svg width="18" height="18" viewBox="0 0 24 24" fill="none" stroke="#1b2a92" stroke-width="2"><rect x="3" y="5" width="18" height="14" rx="2"/><path d="M3 7l9 6 9-6"/></svg></span>
    <span>Info@varomel.com</span>
  </div>
</section>

</body>
</html>
```